Need to design a business card with logo

Hellow
we are a company ,
PT KORAN MELATI JAYA
looking for design of name card.
what we do is property development and management.
design preferable professional corporate look and feel.
corporate. color, pantone colour 289
information required is
company name " Koran Melati Jaya"
person name eg " Peter Walsh"
person title eg "secret agent"
address: 12 heron lane , jakarta, indonesia
phone : +6221 5917264
mobile : 0812 463 518
email : peter@walshmail.example
website: www.peterwa.example
if you want to include logo in the design you are welcome and appreciated , or you can simply use the company name as the logo.
thanks
Target Market(s)
corporate , business person , show events, exhibition events ,etc
Industry/Entity Type
Business
Look and feel
Each slider illustrates characteristics of the customer's brand and the style your logo design should communicate.

```html
<!DOCTYPE html>
<html lang="en">
<head>
<meta charset="utf-8">
<title>Koran Melati Jaya – Business Card</title>
<link rel="stylesheet" href="https://fonts.googleapis.com/css2?family=Tinos:wght@400;700&display=swap">
<style>
  :root {
    --navy: #262850;
    --ink-light: #ffffff;
    --rule-red: #b3392b;
  }
  html, body {
    margin: 0;
    padding: 0;
    width: 1200px;
    height: 480px;
    overflow: hidden;
    background: var(--navy);
  }
  .card {
    position: relative;
    width: 1200px;
    height: 480px;
    background: var(--navy);
    color: var(--ink-light);
    font-family: "Tinos", "Times New Roman", serif;
    overflow: hidden;
  }
  .card p {
    position: absolute;
    margin: 0;
    line-height: 1;
    white-space: nowrap;
  }
  .card__name {
    left: 12px;
    top: 112px;
    font-size: 40px;
    font-weight: 700;
  }
  .card__title {
    left: 12px;
    top: 176px;
    font-size: 40px;
    font-weight: 700;
  }
  .card__online {
    right: 10px;
    top: 186px;
    font-size: 29px;
    font-weight: 400;
  }
  .card__rule {
    position: absolute;
    left: 0;
    top: 235px;
    width: 1200px;
    height: 6px;
    background: var(--rule-red);
  }
  .card__address {
    left: 8px;
    top: 257px;
    font-size: 34px;
    font-weight: 400;
  }
  .card__company {
    left: 12px;
    top: 340px;
    font-size: 40px;
    font-weight: 700;
  }
</style>
</head>
<body>
  <main class="card">
    <p class="card__name">PETER WALSH</p>
    <p class="card__title">AGENT SECRET</p>
    <p class="card__online">PETER@WALSHMAIL.EXAMPLE &nbsp;* WWW.PETERWA.EXAMPLE</p>
    <div class="card__rule"></div>
    <p class="card__address">12 HERON LANE * JAKARTA * INDONESIA * +6221 5917264 * 0812 463 518</p>
    <p class="card__company">KORAN MELATI JAYA</p>
  </main>
</body>
</html>
```